Design a menu for health restaurant

A health food restaurant in Los Angeles is seeking menu design. Our foods are made from scratch using whole ingredients.
Name: Grubb Larder
Address: 1000 E 60th StLos Angeles, CA 90247
Website: www.GrubbLarder.example
We are looking for a clean and simple menu. Brand colors are white/tan, green and orange.

Please see attached excel with menu items and logo. We do not yet have prices.

Colors
f78f20
9bcb3c
ffffff
fff3d1

Requirements
Must have
• Easy to read.
Trifold menu design (front and back).
VEGAN, VEGETARIAN, GLUTEN FREE, CONTAINS NUTS symbols.
Logo.
Nice to have
• Incorporate brand colors, but still be easy to read.
We would like to use the Belco font (attached) if it works. If not we are open to a similar font that is easy to read.

Please see attached images.
We like the images and headers of OPTION 1. Would like something similar in trifold format.
We like the clean fonts of OPTION 2.

```html
<!DOCTYPE html>
<html lang="en">
<head>
<meta charset="utf-8">
<title>Grubb Larder Menu</title>
<link rel="stylesheet" href="https://fonts.googleapis.com/css2?family=Bungee&family=Oswald:wght@500;600&family=Roboto+Condensed:wght@400;700&display=swap">
<style>
  :root {
    --orange: #f78f20;
    --green: #9bcb3c;
    --white: #ffffff;
    --cream: #fbf1c6;
    --ink: #3a3a2e;
  }
  * { box-sizing: border-box; margin: 0; padding: 0; }
  html, body { width: 1200px; height: 967px; overflow: hidden; background: var(--white); }
  body { position: relative; font-family: "Roboto Condensed", Arial, sans-serif; color: var(--ink); }

  .menu-panel { position: absolute; left: 73px; top: 63px; width: 1080px; height: 840px; background: var(--cream); }
  .band { position: absolute; }
  .band-green { background: var(--green); }
  .band-orange { background: var(--orange); }

  .section-title {
    position: absolute; font-family: "Bungee", Impact, sans-serif; font-size: 17px;
    letter-spacing: 0.5px; color: var(--ink); line-height: 1;
  }
  .section-title.orange-text { color: var(--orange); }
  .section-title.light { color: var(--white); }
  .dots { position: absolute; height: 0; border-top: 2px dotted var(--white); }
  .dots.orange { border-top-color: var(--orange); }

  .item { position: absolute; width: 106px; font-size: 10px; line-height: 1.3; }
  .item h3 {
    font-family: "Oswald", "Arial Narrow", sans-serif; font-weight: 600; font-size: 10px;
    text-transform: uppercase; line-height: 1.2; letter-spacing: 0.2px;
  }
  .item .price { display: block; font-size: 9.5px; margin: 2px 0 7px; }
  .item .note { display: block; font-size: 7.5px; }
  .item.light { color: var(--white); }

  .tag {
    display: inline-block; vertical-align: middle; font-family: "Roboto Condensed", sans-serif;
    font-size: 6px; font-weight: 700; line-height: 9px; height: 10px; min-width: 10px;
    text-align: center; border: 1px solid currentColor; margin-left: 1px;
  }
  .tag.vegan, .tag.nuts { border-radius: 50%; }
  .tag.gf { border-radius: 3px; padding: 0 1px; }
  .tag.veg { border: none; font-size: 9px; }

  .photo { position: absolute; border-radius: 6px; }

  .legend {
    position: absolute; left: 800px; top: 827px; width: 318px; height: 26px;
    background: var(--green); display: flex; align-items: center; justify-content: space-around;
    font-size: 8.5px; font-weight: 700; color: var(--ink); text-transform: uppercase;
  }
</style>
</head>
<body>
<main class="menu-panel" aria-label="Grubb Larder menu"></main>

<div class="band band-green" style="left:73px;top:63px;width:367px;height:44px"></div>
<div class="band band-orange" style="left:440px;top:63px;width:347px;height:233px"></div>
<div class="band band-green" style="left:787px;top:63px;width:366px;height:44px"></div>
<div class="band band-green" style="left:440px;top:324px;width:347px;height:20px"></div>
<div class="band band-orange" style="left:73px;top:448px;width:367px;height:17px"></div>
<div class="band band-orange" style="left:787px;top:587px;width:366px;height:20px"></div>

<h2 class="section-title" style="left:103px;top:91px">Breakfast</h2>
<h2 class="section-title light" style="left:570px;top:92px">Combos</h2>
<div class="dots" style="left:460px;top:102px;width:87px"></div>
<div class="dots" style="left:677px;top:102px;width:90px"></div>
<h2 class="section-title" style="left:800px;top:91px">Bowls</h2>
<h2 class="section-title" style="left:451px;top:333px">Burgers N' Sammies</h2>
<h2 class="section-title" style="left:106px;top:456px">Salads</h2>
<h2 class="section-title orange-text" style="left:451px;top:724px">Soups</h2>
<div class="dots orange" style="left:531px;top:734px;width:240px"></div>
<h2 class="section-title" style="left:800px;top:596px">Wraps</h2>

<!-- Breakfast -->
<article class="item" style="left:104px;top:128px"><h3>Avocado Super Toast <span class="tag vegan">VG</span></h3><span class="price">11.99</span><p>Avocado Mash, Tomato, Basil, Ground Flax, Hemp Seed, Chickpeas, and Moringa Powder on Whole Wheat Bread.</p></article>
<article class="item" style="left:216px;top:128px"><h3>Breakfast Sammy <span class="tag vegan">VG</span></h3><span class="price">11.99</span><p>Your choice of over medium egg or tofu steak with guacamole, tomato, and Larder sauce on an English muffin.</p></article>
<article class="item" style="left:328px;top:128px"><h3>Pastries <span class="tag veg">▽</span></h3><span class="price">11.99</span><p>Croissant (regular, almond, chocolate), Blueberry Muffin, Superseed Cookie</p></article>
<article class="item" style="left:328px;top:221px"><h3>Parfait <span class="tag veg">▽</span></h3><span class="price">11.99</span><p>Fresh strawberries and blueberries on yogurt and muesli and topped with honey drizzle.</p></article>
<div class="photo" role="img" aria-label="Photo of avocado toast on a white plate" style="left:327px;top:336px;width:100px;height:75px;background:radial-gradient(circle,#c9a070 0%,#8a9b55 45%,#f4f2ec 75%)"></div>
<article class="item" style="left:104px;top:280px"><h3>Brunch Burger</h3><span class="price">11.99</span><p>House seasoned beef burger topped with an over medium egg, red leaf lettuce, tomato, housemade pickles and Larder Sauce on a bun.</p></article>
<article class="item" style="left:216px;top:280px"><h3>AM Burrito</h3><span class="price">11.99</span><p>Scrambled eggs, onion, red bell pepper, black beans, housemade salsa, yogurt, and pepper jack cheese in a tortilla.</p></article>

<!-- Salads -->
<article class="item" style="left:104px;top:485px"><h3>Avocado, Golden Beet, and Cranberry Salad <span class="tag veg">▽</span><span class="tag gf">GF</span></h3><span class="price">11.99</span><p>Gold beets, avocado, dried cranberries, watermelon radish, red kale, romaine, mixed greens, and pepitas served with Golden Buddha dressing.</p></article>
<article class="item" style="left:216px;top:485px"><h3>Mediterranean Salad <span class="tag veg">▽</span><span class="tag gf">GF</span></h3><span class="price">11.99</span><p>Cucumbers, Kalamata olives, cherry tomatoes, parsley, tricolor quinoa, hard-boiled egg, and hummus on mixed greens, romaine, and red cabbage with lemon-olive oil dressing.</p></article>
<article class="item" style="left:328px;top:485px"><h3>Rancher's Salad <span class="tag veg">▽</span><span class="tag gf">GF</span></h3><span class="price">11.99</span><p>Tomato, red onion, hard boiled egg, avocado, feta cheese, microgreens, and grilled chicken on romaine with Ranch dressing.</p></article>
<article class="item" style="left:216px;top:689px"><h3>Burrata Salad <span class="tag veg">▽</span><span class="tag gf">GF</span></h3><span class="price">11.99</span><p>Tomato, melon, shredded basil, balsamic glaze, fresh cracked pepper, and olive oil with burrata.</p></article>
<article class="item" style="left:328px;top:651px"><h3>Vegan Chef Salad <span class="tag vegan">VG</span><span class="tag gf">GF</span><span class="tag nuts">N</span></h3><span class="price">11.99</span><p>Roasted potatoes and carrots, chickpeas, avocado, microgreens and walnuts on mixed greens, romaine, and red kale with vegan ranch</p></article>
<div class="photo" role="img" aria-label="Photos of two salads in white bowls" style="left:103px;top:680px;width:90px;height:176px;background:linear-gradient(180deg,#f2f0ea 0%,#a8b56a 25%,#f2f0ea 50%,#9caa62 75%,#f2f0ea 100%)"></div>

<!-- Combos -->
<article class="item light" style="left:459px;top:125px"><h3>Soup + Salad</h3><span class="price">11.99</span><p>Your choice of soup and side salad. 16oz soup + 38oz salad</p></article>
<article class="item light" style="left:565px;top:125px"><h3>Avo Toast Combo</h3><span class="price">11.99</span><p>Half avocado toast and your choice of soup. 16oz</p></article>
<article class="item light" style="left:673px;top:125px"><h3>Soup + Sammy</h3><span class="price">11.99</span><p>Your choice of soup and sandwich. 16oz soup + Sandwich</p></article>
<div class="photo" role="img" aria-label="Photo of a bowl of butternut squash soup" style="left:440px;top:229px;width:174px;height:67px;border-radius:0;background:radial-gradient(ellipse at 50% 50%,#d08a3a 0%,#c99354 35%,#e9e6df 60%)"></div>
<div class="photo" role="img" aria-label="Photo of a burger on a plate" style="left:614px;top:229px;width:173px;height:67px;border-radius:0;background:linear-gradient(90deg,#e6e2da,#c08a4a 45%,#8a9a4a 60%,#e6e2da)"></div>

<!-- Burgers -->
<article class="item" style="left:451px;top:372px"><h3>Air Fried Chicken Sammy</h3><span class="price">11.99</span><p>Air fried chicken breast topped with red leaf lettuce, tomato, house made pickles and Larder Sauce on a bun served with choice of salad of fries.</p></article>
<article class="item" style="left:563px;top:372px"><h3>Classic Beef Burger</h3><span class="price">11.99</span><p>House seasoned beef burger topped with red leaf lettuce, tomato, cheddar cheese, house made pickles and Larder Sauce on a bun served with choice of salad of fries.</p></article>
<article class="item" style="left:675px;top:372px"><h3>Salmon Burger</h3><span class="price">11.99</span><p>House made salmon burger topped with red leaf lettuce, tomato, house made pickles and Larder yogurt on a bun served with choice of salad of fries.</p></article>
<article class="item" style="left:451px;top:537px"><h3>Grilled Chicken Sammy</h3><span class="price">11.99</span><p>Grilled chicken topped with guacamole, red leaf lettuce, tomato, house made pickles and Larder Sauce. Served with regular fries or side salad.</p></article>
<article class="item" style="left:563px;top:549px"><h3>Black Bean Pine Nut Burger <span class="tag vegan">VG</span><span class="tag nuts">N</span></h3><span class="price">11.99</span><p>House made black bean pine nut burger topped with red leaf lettuce, tomato, house made pickles and mustard aioli on a bun served with choice of salad of fries.</p></article>
<div class="photo" role="img" aria-label="Photos of two burgers on white plates" style="left:683px;top:529px;width:92px;height:178px;border-radius:0;background:linear-gradient(180deg,#eeebe4 0%,#c89a5c 25%,#eeebe4 50%,#d9a048 75%,#eeebe4 100%)"></div>

<!-- Soups -->
<article class="item" style="left:451px;top:753px"><h3>Chicken Noodle <span class="tag gf">GF</span></h3><span class="price">11.99</span><p>Chicken, egg noodles, root vegetables, oregano &amp; peppercorns.</p></article>
<article class="item" style="left:563px;top:753px"><h3>Larder Chili <span class="tag gf">GF</span></h3><span class="price">11.99</span><p>Chicken, onions, bell peppers, jalapeños, black &amp; kidney beans, and tomato.</p></article>
<article class="item" style="left:675px;top:753px"><h3>Seasonal Rotating</h3><span class="note">(Butternut Squash Soup)</span><span class="tag gf">GF</span><span class="tag vegan">VG</span><span class="price">11.99</span><p>Butternut squash blended with warm spices, and coconut milk.</p></article>

<!-- Bowls -->
<article class="item" style="left:800px;top:124px"><h3>Southwest Bowl <span class="tag gf">GF</span><span class="tag nuts">N</span></h3><span class="price">11.99</span><p>Your choice of protein with corn, black beans, red onions, almonds and avocado over quinoa with lime hot sauce.</p></article>
<article class="item" style="left:912px;top:124px"><h3>Hollywood Bowl <span class="tag gf">GF</span></h3><span class="price">11.99</span><p>Your choice of protein with broccoli, roasted corn, cherry tomatoes, basil, pepitas, flax seeds and lemon juice on wild and brown rice.</p></article>
<article class="item" style="left:1024px;top:124px"><h3>Buddha Bowl</h3><span class="price">11.99</span><p>Your choice of protein with corn, red kale, sweet potatoes, red cabbage, parsley, oregano, hummus, and farro.</p></article>
<article class="item" style="left:800px;top:276px"><h3>Chimi Bowl <span class="tag gf">GF</span></h3><span class="price">11.99</span><p>Your choice of protein with red bell pepper, mushrooms, zucchini, squash, onion, cherry tomatoes and fresh herb chimichurri on wild and brown rice.</p></article>
<article class="item" style="left:912px;top:276px"><h3>Larder Bowl <span class="tag gf">GF</span></h3><span class="price">11.99</span><p>Your choice of protein with roasted chickpeas and cauliflower, zesty fennel salad and citrus yogurt.</p></article>
<article class="item" style="left:1024px;top:263px"><h3>Chili Rice Bowl <span class="tag gf">GF</span></h3><span class="price">11.99</span><p>Chicken, onions, bell peppers, jalapeños, black &amp; kidney beans, and tomato over brown rice.</p></article>
<article class="item" style="left:800px;top:428px"><h3>Soba Noodle Bowl</h3><span class="price">11.99</span><p>Your choice of protein with spinach, snow peas, roasted carrots, red bell pepper, cilantro, sesame seeds and ginger lime sauce over soba noodles.</p></article>
<div class="photo" role="img" aria-label="Photo of a soba noodle bowl with carrots and snow peas" style="left:911px;top:396px;width:212px;height:165px;border-radius:0;background:radial-gradient(ellipse at 50% 50%,#5a4a3a 0%,#e0703a 30%,#7fa356 45%,#f3f1ec 70%)"></div>

<!-- Wraps -->
<article class="item" style="left:800px;top:627px"><h3>Rancher's Wrap</h3><span class="price">11.99</span><p>Tomato, red onion, hard boiled egg, avocado, feta cheese, microgreens, romaine, grilled chicken and Ranch dressing in a grilled wrap.</p></article>
<article class="item" style="left:912px;top:627px"><h3>Vegan Tuna Wrap <span class="tag vegan">VG</span></h3><span class="price">11.99</span><p>Vegan tuna, romaine, avocado, celery, shallot, and oregano with Green Herb Sauce in a whole grain wrap.</p></article>
<article class="item" style="left:1024px;top:627px"><h3>Vegetarian Wrap <span class="tag veg">▽</span></h3><span class="price">11.99</span><p>Roasted chickpeas, romaine, avocado, red bell pepper, shaved carrots, cucumber, spinach, basil, black beans and feta with lemon-hummus in a sprouted 7-grain wrap.</p></article>

<div class="legend">
  <span><span class="tag veg">▽</span>Vegetarian</span>
  <span><span class="tag vegan">VG</span> Vegan</span>
  <span><span class="tag nuts">N</span> Contains Nuts</span>
  <span><span class="tag gf">GF</span> Gluten-Free</span>
</div>
</body>
</html>
```